Relaunch Instagram Posts Design

We want to give you a better understanding about the expected outcome of this task, and give you a little bit of a background that should help you throughout.
We already have social media accounts, they aren’t active and the posts are outdated. We just finished our rebranding exercise, and accordingly we are planning to have a re-launch where we communicate our new identity, and rebuild our online existence, to enhance our social media presence and engagement.
Thus, we want to formulate the style of posting from the beginning, so that it reflects the identity overall and we can move forward with in a consistent manner.

Find attached details. We will share other files later. You need to read the attachment in the project to understand the requirement. Also, you should use the attached images in the project. You should also use products images from our website...www.bloomvantra.com
Our Primary color is #5725A9, PURPLE (based on color HEX Code)
Our Secondary colors #7C50BE, #A17BD3, #C5A6E8, #EAD1FD
Also, this secondary colors can be used #2B9348, #55A630, #80B918, #AACC00

Target Market(s)

Gift-givers who would like to bring a gift of value and meaning, representing the occasion

Industry/Entity Type

Flowers

Colors

Designer to choose colors to be used in the design.

Requirements
Must have
• Image based posts with little graphics + typography-based posts.... hammer on the emotional aspect, focusing on special moments such as using images related nice moments
Nice to have
• A full overview as in the brief (with all 21 posts), to give the sense of the design direction for us to know if it fits our new brand vision or not.
Should not have
• A typical commercial design direction that focuses so much on direct product communication. This definitely will be there, but we want this to be integrated with the other aspects.

```html
<!DOCTYPE html>
<html lang="en">
<head>
<meta charset="utf-8">
<title>Bloomvantra – Relaunch Posts</title>
<link href="https://fonts.googleapis.com/css2?family=Crimson+Pro:wght@400;500;600&family=Montserrat:wght@400&family=Kalam:wght@400;700&family=Fira+Sans:ital,wght@1,700&display=swap" rel="stylesheet">
<style>
  :root{
    --board:#252525;
    --paper:#ffffff;
    --purple:#7c50be;
    --purple-deep:#5725a9;
    --green:#55a630;
    --green-bright:#80b918;
    --ink-grey:#8a8a8a;
    --serif:"Crimson Pro", Georgia, serif;
    --sans:"Montserrat", Arial, sans-serif;
    --script:"Kalam", cursive;
  }
  *{box-sizing:border-box;margin:0;padding:0}
  html,body{width:1200px;height:652px;overflow:hidden;background:var(--board)}
  .board{position:relative;width:1200px;height:652px}
  .post{position:absolute;background:var(--paper);overflow:hidden}
  .abs{position:absolute}
  .photo{position:absolute}
  .brand{position:absolute;font-family:var(--sans);font-weight:400;letter-spacing:.08em;line-height:1;display:flex;align-items:center;gap:5px}
  .brand .dot{border-radius:50%;display:inline-block}
  .socials{position:absolute;display:flex;align-items:center}
  .socials .icon{border-radius:50%;display:inline-block}
  .handle{font-family:var(--serif)}

  /* post 1 */
  .p1{left:45px;top:56px;width:540px;height:540px}
  .p1 .photo{left:18px;top:19px;width:503px;height:382px;background:radial-gradient(circle at 45% 40%,#f1d6c4 0,#d9c3b6 25%,#a7a09c 55%,#707a6c 80%,#9b9a9e 100%)}
  .p1 .brand{left:40px;top:46px;font-size:10px;color:#fff}
  .p1 .title-box{left:41px;top:324px;width:256px;height:135px;background:var(--purple);color:#fff;font-family:var(--serif);font-weight:500;font-size:60px;line-height:.98;padding:8px 0 0 15px}
  .p1 .tag-box{left:41px;top:459px;width:256px;height:49px;background:var(--green);color:#fff;font-family:var(--serif);font-size:15px;line-height:1.2;padding:5px 11px}
  .p1 .socials{left:341px;top:425px;gap:14px}
  .p1 .icon{width:40px;height:40px;background:var(--purple-deep)}
  .p1 .handle{left:374px;top:470px;font-size:17px;color:var(--purple-deep)}

  /* post 2 */
  .p2{left:615px;top:56px;width:254px;height:254px}
  .p2 .panel{left:8px;top:9px;width:126px;height:237px;background:var(--purple)}
  .p2 .brand{left:17px;top:22px;font-size:7px;color:#fff}
  .p2 .script{left:15px;top:68px;font-family:var(--script);color:#fff;line-height:1}
  .p2 .l1{font-size:18px}
  .p2 .l2{color:var(--green-bright);font-size:20px;margin-left:24px}
  .p2 .l3{color:var(--green-bright);font-size:32px;font-weight:700;margin-left:-3px}
  .p2 .last{left:12px;top:138px;font-family:var(--serif);font-style:italic;font-weight:600;font-size:13px;color:#fff}
  .p2 .rule{left:12px;top:160px;width:108px;height:2px;background:#fff;border-radius:2px;transform:rotate(-3deg)}
  .p2 .band{left:8px;top:183px;width:126px;height:30px;background:var(--green);color:#fff;font-family:var(--serif);font-size:7.5px;line-height:1.2;padding:5px 17px}
  .p2 .socials{left:25px;top:225px;gap:7px}
  .p2 .icon{width:6px;height:6px;background:#fff}
  .p2 .handle{font-size:6.5px;color:#fff;margin-left:2px}
  .p2 .photo{left:141px;top:9px;width:105px;height:237px;background:linear-gradient(90deg,#fff 0,#fff 20%,#2b2b2b 20%,#151515 50%,#f6f6f6 50%,#fff 100%)}

  /* post 3 */
  .p3{left:900px;top:56px;width:255px;height:254px}
  .p3 .photo{left:9px;top:19px;width:238px;height:143px;background:linear-gradient(180deg,#e8e6ea 0,#d9d2c8 45%,#c9ab7e 70%,#bc9f73 100%)}
  .p3 .label{left:120px;top:142px;width:110px;height:24px;background:var(--green);color:#fff;font-family:var(--serif);font-size:13.5px;padding:1px 8px}
  .p3 .title{left:120px;top:166px;width:110px;height:49px;background:var(--purple);color:#fff;font-family:var(--serif);font-weight:500;font-size:24px;line-height:.95;padding:2px 8px}
  .p3 .brand{left:25px;top:189px;font-size:7px;color:var(--purple)}
  .p3 .socials{left:22px;top:223px;gap:4px}
  .p3 .icon{width:10px;height:10px;background:var(--purple-deep)}
  .p3 .handle{font-size:6.5px;color:var(--purple-deep);margin-left:2px}
  .p3 .body{left:121px;top:219px;width:112px;font-family:var(--serif);font-size:5.2px;line-height:1.4;color:var(--ink-grey)}

  /* post 4 */
  .p4{left:615px;top:342px;width:254px;height:254px}
  .p4 .frame-v{left:7px;top:24px;width:7px;height:102px;background:var(--purple)}
  .p4 .frame-h{left:7px;top:121px;width:112px;height:5px;background:var(--purple)}
  .p4 .photo.a{left:28px;top:26px;width:79px;height:88px;background:radial-gradient(circle,#c8272a 0,#a01c20 35%,#e9e9e9 60%,#fff 80%)}
  .p4 .logo-box{left:120px;top:24px;width:126px;height:48px;background:var(--purple)}
  .p4 .brand{left:30px;top:16px;font-size:8px;color:#fff}
  .p4 .photo.b{left:153px;top:82px;width:75px;height:128px;background:linear-gradient(180deg,#fff 0,#b52a35 20%,#e8c9a8 55%,#f2efe8 80%,#fff 100%)}
  .p4 .title{left:18px;top:141px;width:95px;text-align:center;font-family:"Fira Sans",Arial,sans-serif;font-style:italic;font-weight:700;color:var(--purple);font-size:21px;line-height:1.25}
  .p4 .body{left:20px;top:198px;width:92px;text-align:center;font-family:var(--serif);font-size:6.5px;line-height:1.4;color:var(--ink-grey)}
  .p4 .btn{left:158px;top:215px;width:63px;height:24px;background:var(--purple);border-radius:3px;overflow:hidden}
  .p4 .btn-top{height:11px;background:var(--green);display:flex;gap:6px;justify-content:center;align-items:center}
  .p4 .btn-top i{width:4px;height:4px;border-radius:50%;background:#fff;display:block}
  .p4 .btn-handle{color:#fff;font-family:var(--serif);font-size:4px;letter-spacing:.15em;text-align:center;line-height:12px}

  /* post 5 */
  .p5{left:898px;top:340px;width:255px;height:254px}
  .p5 .photo.a{left:22px;top:23px;width:77px;height:121px;background:radial-gradient(ellipse at 50% 50%,#a02024 0,#c9884e 30%,#efe4cd 60%,#fbf8f1 100%);border-radius:45% 45% 30% 30%}
  .p5 .panel{left:121px;top:9px;width:125px;height:147px;background:var(--purple)}
  .p5 .panel-line{left:108px;top:6px;width:1px;height:56px;background:var(--green-bright)}
  .p5 .panel-line2{left:63px;top:6px;width:46px;height:1px;background:var(--green-bright)}
  .p5 .did{left:22px;top:10px;font-family:var(--serif);font-size:25px;color:#fff;line-height:1}
  .p5 .you{left:28px;top:36px;font-family:var(--script);font-weight:700;font-size:30px;color:var(--green-bright);line-height:1}
  .p5 .know{left:22px;top:76px;font-family:var(--serif);font-size:25px;color:#fff;line-height:1}
  .p5 .body{left:20px;top:114px;width:104px;font-family:var(--serif);font-size:7.8px;line-height:1.7;color:#fff}
  .p5 .brand{left:28px;top:180px;font-size:8px;color:var(--purple)}
  .p5 .bar{left:9px;top:213px;width:111px;height:30px;background:var(--green)}
  .p5 .socials{left:20px;top:222px;gap:6px}
  .p5 .icon{width:11px;height:11px;background:#fff}
  .p5 .handle{font-size:7.5px;color:#fff;margin-left:3px}
  .p5 .photo.b{left:145px;top:168px;width:80px;height:70px;background:linear-gradient(160deg,#fff 0,#d6b04a 30%,#4a3d2a 65%,#fff 100%)}
</style>
</head>
<body>
<main class="board">

  <section class="post p1">
    <div class="photo" role="img" aria-label="Bouquet of pale peach roses with white blossoms"></div>
    <div class="brand"><span>BLOOMVANTRA</span><span class="dot" style="width:9px;height:9px;border:1px solid #fff"></span></div>
    <h1 class="abs title-box">Fresh<br>Flowers</h1>
    <p class="abs tag-box">Lorem ipsum dolor sit amet, consec-<br>tetuer adipiscing elit, sed diam.</p>
    <div class="socials"><span class="icon"></span><span class="icon"></span><span class="icon"></span></div>
    <p class="abs handle">@username</p>
  </section>

  <section class="post p2">
    <div class="abs panel">
    </div>
    <div class="brand" style="left:25px;top:31px;font-size:7px;color:#fff">BLOOMVANTRA</div>
    <div class="abs script" style="left:23px;top:72px">
      <div class="l1">Helping</div>
      <div class="l2">Nature's</div>
      <div class="l3">Beauty</div>
    </div>
    <p class="abs last" style="left:20px;top:138px">Last Forever</p>
    <div class="abs rule" style="left:20px"></div>
    <p class="abs band">Fresh flowers &amp;<br>gifts for all occasions</p>
    <div class="socials"><span class="icon"></span><span class="icon"></span><span class="icon"></span><span class="handle">@username</span></div>
    <div class="photo" role="img" aria-label="Single preserved red rose beside its black gift box"></div>
  </section>

  <section class="post p3">
    <div class="photo" role="img" aria-label="Florist's hands arranging a small plate of pink roses on a workbench"></div>
    <p class="abs label">High Quality &amp;</p>
    <h2 class="abs title">Fresh<br>Flowers</h2>
    <div class="brand"><span>BLOOMVANTRA</span><span class="dot" style="width:9px;height:9px;background:var(--purple)"></span></div>
    <div class="socials"><span class="icon"></span><span class="icon"></span><span class="icon"></span><span class="handle">@username</span></div>
    <p class="abs body">Lorem ipsum dolor sit amet, consectetuer adipiscing elit, sed diam. dolor sit amet,</p>
  </section>

  <section class="post p4">
    <div class="abs frame-v"></div>
    <div class="abs frame-h"></div>
    <div class="photo a" role="img" aria-label="Red roses preserved in a glass bowl"></div>
    <div class="abs logo-box"><div class="brand">BLOOMVANTRA</div></div>
    <div class="photo b" role="img" aria-label="Red rose on a curved gold stem set in a crystal base"></div>
    <h2 class="abs title">Flowers<br>for You</h2>
    <p class="abs body">Lorem ipsum dolor sit amet, conse tetuer adipiscing elit, sed diam. consectetuer adipiscing elit, sed diam.</p>
    <div class="abs btn"><div class="btn-top"><i></i><i></i><i></i></div><div class="btn-handle">@username</div></div>
  </section>

  <section class="post p5">
    <div class="photo a" role="img" aria-label="Red roses encased in a faceted crystal block"></div>
    <div class="abs panel">
      <div class="abs panel-line"></div>
      <div class="abs panel-line2"></div>
      <p class="abs did">DID</p>
      <p class="abs you">You</p>
      <p class="abs know">KNOW?</p>
      <p class="abs body">Lorem ipsum dolor sit amet, consectetuer adipiscing elit.</p>
    </div>
    <div class="brand"><span>BLOOMVANTRA</span><span class="dot" style="width:9px;height:9px;background:var(--purple)"></span></div>
    <div class="abs bar"></div>
    <div class="socials"><span class="icon"></span><span class="icon"></span><span class="icon"></span><span class="handle">@username</span></div>
    <div class="photo b" role="img" aria-label="Gold-plated rose with its presentation box"></div>
  </section>

</main>
</body>
</html>
```